Wordpress Design for a Digital Management Consulting Business

I need a simple Wordpress Design and someone to set it up for a new boutique management consulting business called Tidewell Advisory that specialises in providing strategic advice to help grow digital businesses. It covers business strategy, marketing strategy, digital strategy, web product development, marketing campaigns, social, search, etc. From strategy to implementation.

URL is: tidewelladvisory.com.au

My professional background is here: au.examplenet.com/in/norabellweather

Competitors: other boutique digital/marketing management consulting businesses in Australia

The logos, colours and fonts are attached.

I would like the site to convey a business that is Smart/intelligent, Contemporary, Progressive, Digital, Energetic, Friendly.

The objective of the site is to educate visitors about what Tidewell Advisory does and encourage them to contact me for more information. It will be very light on content.

Target Market(s)

CEOs/Managing Directors, General Managers, Marketing Directors

Industry/Entity Type

Management Consulting

Font styles to use
Sans Serif

Colors
e34197
5c5c5c
000000

Requirements
Must have
• Site design requirements:
• Choose an appropriate Wordpress template, set it up for me and let me be able to edit it ongoing.
• It should use lots of images - these can be inspirational and not necessarily tied directly to the work
• Pink should feature, but not be the dominant colour.
• Site structure should be:
• 1. Home page - image led with horizontal navigation. Text beneath and images to describe the services.
• 2. About page - with space to write text and insert a picture of the Director
• 3. Services - with space to highlight services either as a list or graphically with text
• 4. Contact page - with space to write text and add email links, etc.
• Should have horizontal navigation
• It should have the flexibility to add another page
Nice to have
• Use the tree icon somehow in the design - consider in the background enlarged
• Use pink, grey, black from logo. Can introduce another complimentary colour if necessary.
• Can introduce another complimentary font to go with the logo font.
Should not have
• Use cliched business images and icons, eg. business suits, hand shakes, business men, business ties.

```html
<!DOCTYPE html>
<html lang="en">
<head>
<meta charset="utf-8">
<title>Tidewell Advisory</title>
<link rel="stylesheet" href="https://fonts.googleapis.com/css2?family=Questrial&family=Open+Sans:wght@400;600&display=swap">
<style>
:root{
  --pink:#e34197;
  --grey:#5c5c5c;
  --black:#000000;
  --light:#f2f2f2;
  --hero-a:#f4f4f4;
  --hero-b:#d9d9d9;
  --dark:#262626;
  --footer:#3b3b3b;
  --footer-bar:#2e2e2e;
  --muted:#9a9a9a;
}
*{box-sizing:border-box;margin:0;padding:0}
html,body{width:861px;height:1200px;overflow:hidden;background:#fff}
body{font-family:"Open Sans",Arial,sans-serif;color:var(--grey);position:relative}
.heading{font-family:"Questrial",Arial,sans-serif}

/* header */
.site-header{position:absolute;top:0;left:0;width:861px;height:64px;background:#fff;z-index:2}
.brand{position:absolute;left:172px;top:22px;display:flex;align-items:center;gap:7px;font-family:"Questrial",Arial,sans-serif;font-size:13px;letter-spacing:2px;color:var(--pink);text-transform:uppercase}
.brand-dot{width:12px;height:12px;border-radius:50%;background:var(--pink)}
.main-nav{position:absolute;right:170px;top:20px;display:flex;gap:6px}
.main-nav a{font-family:"Questrial",Arial,sans-serif;font-size:8px;letter-spacing:1px;color:var(--grey);text-decoration:none;padding:5px 10px;text-transform:uppercase}
.main-nav a.active{border:1px solid var(--pink);color:var(--pink)}

/* hero */
.hero{position:absolute;top:64px;left:0;width:861px;height:243px;overflow:hidden}
.hero-photo{position:absolute;inset:0;background:linear-gradient(100deg,var(--hero-a) 0%,#ececec 50%,var(--hero-b) 100%)}
.hero-title{position:absolute;left:172px;top:36px;font-size:44px;line-height:46px;color:var(--pink);letter-spacing:1px;text-transform:uppercase}
.hero-text{position:absolute;left:172px;top:132px;width:290px;font-size:7.5px;line-height:12px;color:var(--grey)}
.hero-btn{position:absolute;left:172px;top:180px;border:1px solid var(--grey);color:var(--grey);font-size:7px;letter-spacing:1px;padding:5px 12px;text-transform:uppercase}
.slider-dots{position:absolute;left:412px;top:224px;display:flex;gap:5px}
.slider-dots span{width:6px;height:6px;border-radius:50%;background:#bdbdbd}
.slider-dots span.on{background:var(--pink)}

/* services */
.services{position:absolute;top:307px;left:0;width:861px;height:281px;background:#fff}
.section-title{position:absolute;left:172px;top:22px;font-size:14px;letter-spacing:1px;color:var(--pink);text-transform:uppercase}
.section-rule{position:absolute;left:172px;top:44px;width:518px;height:1px;background:#e4c2d4}
.card{position:absolute;width:122px;text-align:center}
.card-photo{width:122px;height:58px;background:linear-gradient(135deg,#dcdcdc,#9d9d9d)}
.card-title{margin-top:9px;font-size:7.5px;letter-spacing:.5px;color:var(--pink);text-transform:uppercase}
.card-text{margin:6px auto 0;width:108px;font-size:6.5px;line-height:10px;color:var(--grey)}
.btn-pink{display:inline-block;margin-top:14px;background:var(--pink);color:#fff;font-size:6.5px;letter-spacing:.5px;padding:6px 18px;text-transform:uppercase}
.services .card{top:74px}

/* what we do */
.what-we-do{position:absolute;top:588px;left:0;width:861px;height:273px;overflow:hidden}
.wwd-photo{position:absolute;inset:0;background:linear-gradient(90deg,#1c1c1c 0%,#3c3c3c 45%,#2a2a2a 70%,#4a4a4a 100%)}
.wwd-title{position:absolute;left:0;width:861px;top:24px;text-align:center;font-size:14px;letter-spacing:1px;color:#fff;text-transform:uppercase}
.what-we-do .card{top:70px}
.what-we-do .card-photo{border:3px solid #fff;background:linear-gradient(135deg,#dfe7f0,#8ea3bb)}
.what-we-do .card-title{color:#fff}
.what-we-do .card-text{color:#cfcfcf}
.btn-ghost{display:inline-block;margin-top:12px;border:1px solid #8a8a8a;color:#e6e6e6;font-size:6.5px;letter-spacing:.5px;padding:5px 16px;text-transform:uppercase}

/* about */
.about{position:absolute;top:861px;left:0;width:861px;height:224px;background:#fff}
.about-photo{position:absolute;left:200px;top:12px;width:202px;height:212px;background:linear-gradient(180deg,#efe9e4,#c9c3bf)}
.about-title{position:absolute;left:445px;top:30px;font-size:12px;letter-spacing:1px;color:var(--pink);text-transform:uppercase}
.about-text{position:absolute;left:445px;top:56px;width:245px;font-size:6.8px;line-height:10.5px;color:var(--grey)}
.about-text p{margin-bottom:8px}
.about .btn-pink{position:absolute;left:608px;top:182px;margin:0}

/* footer */
.site-footer{position:absolute;top:1085px;left:0;width:861px;height:115px;background:var(--footer)}
.footer-col{position:absolute;top:22px;font-size:6.5px;line-height:11px;color:var(--muted)}
.footer-col h4{font-weight:600;color:#d0d0d0;font-size:7px;margin-bottom:3px}
.footer-links{left:172px}
.footer-contact{left:300px}
.contact-row{display:flex;align-items:center;gap:5px}
.social{position:absolute;left:448px;top:32px;display:flex;gap:4px}
.social span{width:12px;height:12px;border-radius:50%;background:var(--muted)}
.social span.pink{background:var(--pink)}
.footer-brand{position:absolute;left:560px;top:34px;font-family:"Questrial",Arial,sans-serif;font-size:12px;letter-spacing:2px;color:#6e6e6e;text-transform:uppercase}
.footer-bar{position:absolute;bottom:0;left:0;width:861px;height:20px;background:var(--footer-bar);text-align:center;font-size:6px;line-height:20px;color:#7d7d7d}
</style>
</head>
<body>

<header class="site-header">
  <div class="brand"><span class="brand-dot"></span>Tidewell Advisory</div>
  <nav class="main-nav">
    <a class="active" href="#">Home</a>
    <a href="#">Services</a>
    <a href="#">About Me</a>
    <a href="#">News</a>
    <a href="#">Contact</a>
  </nav>
</header>

<section class="hero">
  <div class="hero-photo" role="img" aria-label="Bright desk scene with an open laptop and a cup of coffee on a pale grey surface"></div>
  <h1 class="hero-title heading">Tidewell<br>Advisory</h1>
  <p class="hero-text">We help growing digital businesses find clear direction, from sharp strategy to confident delivery across marketing, product, social and search, so every decision moves you forward.</p>
  <span class="hero-btn">Read More</span>
  <div class="slider-dots"><span class="on"></span><span></span></div>
</section>

<section class="services">
  <h2 class="section-title heading">Services</h2>
  <div class="section-rule"></div>
  <article class="card" style="left:207px">
    <div class="card-photo" role="img" aria-label="Strategy board game pieces"></div>
    <h3 class="card-title">Global Strategy</h3>
    <p class="card-text">Shape a growth plan that fits your market and keeps the whole team aligned.</p>
    <span class="btn-pink">Read More</span>
  </article>
  <article class="card" style="left:370px">
    <div class="card-photo" role="img" aria-label="Laptop, tablet and phone showing a website"></div>
    <h3 class="card-title">Marketing Strategy</h3>
    <p class="card-text">Reach the right people with campaigns built on insight, data and clear positioning.</p>
    <span class="btn-pink">Read More</span>
  </article>
  <article class="card" style="left:533px">
    <div class="card-photo" role="img" aria-label="Glowing digital network on a dark background" style="background:linear-gradient(135deg,#3a3a3a,#111)"></div>
    <h3 class="card-title">Digital Transformation</h3>
    <p class="card-text">Move your products, channels and processes online with a roadmap you can trust.</p>
    <span class="btn-pink">Read More</span>
  </article>
</section>

<section class="what-we-do">
  <div class="wwd-photo" role="img" aria-label="Dark background of a hand sketching ideas and diagrams"></div>
  <h2 class="wwd-title heading">What We Do</h2>
  <article class="card" style="left:207px">
    <div class="card-photo" role="img" aria-label="Hands working over planning notes"></div>
    <h3 class="card-title">Strategic Thinking</h3>
    <p class="card-text">We look beyond the next quarter to find lasting advantage for your business.</p>
    <span class="btn-ghost">Read More</span>
  </article>
  <article class="card" style="left:370px">
    <div class="card-photo" role="img" aria-label="Charts and reports on a desk"></div>
    <h3 class="card-title">Analytical Approach</h3>
    <p class="card-text">Every recommendation rests on evidence, research and measurable results you can track.</p>
    <span class="btn-ghost">Read More</span>
  </article>
  <article class="card" style="left:533px">
    <div class="card-photo" role="img" aria-label="Team meeting around a table"></div>
    <h3 class="card-title">Execution &amp; Implementation</h3>
    <p class="card-text">From first plan to final launch, we stay with you until the work is done.</p>
    <span class="btn-ghost">Read More</span>
  </article>
</section>

<section class="about">
  <div class="about-photo" role="img" aria-label="Portrait of the director pointing towards the about text"></div>
  <h2 class="about-title heading">About Tidewell</h2>
  <div class="about-text">
    <p>Tidewell Advisory is a boutique consultancy that helps digital businesses grow with purpose. We combine strategy, marketing and product thinking to turn ambitious goals into practical plans.</p>
    <p>Our director has led growth teams across media, retail and technology, and now partners with CEOs and marketing leaders who want clear advice and hands-on support.</p>
    <p>Get in touch to talk about where your business is heading next.</p>
  </div>
  <span class="btn-pink">Read More</span>
</section>

<footer class="site-footer">
  <div class="footer-col footer-links">
    <h4>Quick Links</h4>
    <div>Home</div><div>Services</div><div>About Me</div><div>Contact</div>
  </div>
  <div class="footer-col footer-contact">
    <div class="contact-row">
      <svg width="8" height="8" viewBox="0 0 10 10"><circle cx="5" cy="5" r="4" fill="none" stroke="#9a9a9a"/><path d="M1 5h8M5 1c2 2 2 6 0 8M5 1c-2 2-2 6 0 8" fill="none" stroke="#9a9a9a" stroke-width=".7"/></svg>
      tidewelladvisory.com.au
    </div>
    <div class="contact-row">
      <svg width="8" height="8" viewBox="0 0 10 10"><rect x="1" y="1" width="8" height="8" fill="none" stroke="#9a9a9a"/></svg>
      au.examplenet.com/in/norabellweather
    </div>
    <div class="contact-row">
      <svg width="8" height="8" viewBox="0 0 10 10"><path d="M5 9.5C2.5 6.5 2 5 2 4a3 3 0 0 1 6 0c0 1-.5 2.5-3 5.5z" fill="#9a9a9a"/></svg>
      Melbourne, Australia
    </div>
  </div>
  <div class="social" aria-label="Social links"><span class="pink"></span><span></span><span></span><span class="pink"></span></div>
  <div class="footer-brand">Tidewell Advisory</div>
  <div class="footer-bar">© 2024 Tidewell Advisory. All rights reserved.</div>
</footer>

</body>
</html>
```